In need of a fabulous a newsletter template!

We would like a Newsletter template designed for our practice that we can use on a quarterly basis to send out to our patients via email. This template should also be printable so we may have it printed for our waiting area and use for mailings. We envision a single page, double-sided. We would like to be able to fill out the template with out own material, but have a consistent layout with the following sections: 1) Patient Spotlight, 2) Upcoming Events, 3) Technology Update, 4) Pediatric Corner, 5) Exciting news, 6) Learn to Listen, 7) A note from Dr. Fenwick. To view more about our company, visit our website at www.orchardvalehearing.example

Target Market(s)

Our patients --- Adults age 35-90

Industry/Entity Type

Healthcare

Font styles to use
Serif
Sans Serif

Colors
0892cd
34a7d8
0355a3
3377b5
85cae6

Requirements
Must have
• Eye-catching, organized, easy-to-follow layout so that we may send out information to our patients on a quarterly basis. Once created, we need to be able to fill in the information for the sections listed above. Must list our address and contact information on the front and back; probably in the header on the front and footer on the back.
Nice to have
• Sections 1-5 are needed from above, but would like to fit in sections 6-7, if available.

```html
<!DOCTYPE html>
<html lang="en">
<head>
<meta charset="utf-8">
<title>Hearing Care For All Ages – Newsletter</title>
<link rel="stylesheet" href="https://fonts.googleapis.com/css2?family=Nunito+Sans:ital,wght@0,400;0,700;0,800;0,900;1,400&family=PT+Sans+Narrow:wght@400;700&family=Arimo:wght@400&display=swap">
<style>
  :root{
    --teal:#407e8f;
    --teal-dark:#356b7a;
    --turquoise:#2cbcbf;
    --sky:#eaf6fb;
    --grey:#e3e3e3;
    --ink:#3d3d3d;
    --white:#ffffff;
    --backdrop:#d9d9d6;
  }
  *{box-sizing:border-box;margin:0;padding:0}
  html,body{width:1200px;height:900px;overflow:hidden}
  body{background:var(--backdrop);position:relative;font-family:"Nunito Sans",sans-serif;color:var(--ink)}
  .page{position:absolute;top:22px;width:515px;height:844px;background:var(--white);box-shadow:3px 4px 10px rgba(0,0,0,.25);overflow:hidden}
  .page--front{left:72px}
  .page--back{left:612px}
  .abs{position:absolute}

  /* front header */
  .brand{position:absolute;display:flex;align-items:center;gap:6px;font-weight:700;color:var(--teal);letter-spacing:.3px;white-space:nowrap}
  .brand__dot{width:10px;height:10px;border-radius:50%;background:var(--turquoise);flex:none}
  .front-brand{left:30px;top:70px;font-size:12px}
  .masthead__title{right:17px;top:44px;font-size:19px;font-weight:800;color:var(--teal);white-space:nowrap}
  .masthead__title span{font-weight:400}
  .masthead__label{right:17px;top:70px;font-size:10px;font-weight:800;color:var(--turquoise)}
  .social-row{display:flex;gap:14px}
  .front-socials{right:17px;top:94px}
  .social{display:flex;align-items:center;gap:5px;font-size:7px;color:var(--ink);white-space:nowrap}
  .social__icon{width:15px;height:15px;border-radius:50%;background:var(--turquoise);flex:none}
  .edition-bar{top:122px;height:18px;background:var(--teal)}
  .edition-bar--a{left:0;width:68px}
  .edition-bar--b{left:73px;width:65px;background:var(--turquoise)}
  .edition-bar--c{left:141px;width:374px;display:flex;justify-content:space-between;align-items:center;padding:0 17px 0 11px;color:var(--white);font-size:10px;font-weight:800;font-family:"PT Sans Narrow",sans-serif;letter-spacing:.3px}
  .edition-bar--c span{font-size:11.5px}

  .spotlight{left:0;top:156px;width:515px;height:230px;background:var(--teal)}
  .section-title{font-weight:800;font-size:21px;color:var(--white);letter-spacing:.3px}
  .spotlight .section-title{position:absolute;left:25px;top:18px}
  .spotlight__photo{left:26px;top:57px;width:145px;height:145px;border:2px solid var(--white);background:linear-gradient(160deg,#8a6a55 0%,#5d4a40 45%,#2f3a42 100%)}
  .spotlight__text{left:198px;top:62px;width:295px;font-size:9.6px;line-height:1.38;color:var(--white);text-align:justify}

  .evaluation{left:0;top:386px;width:515px;height:107px;text-align:center}
  .evaluation h2{margin-top:18px;font-size:23px;font-weight:800;color:var(--ink)}
  .evaluation p{font-size:10.5px;margin-top:2px}
  .evaluation__phone{display:inline-block;margin-top:12px;width:139px;height:20px;line-height:20px;background:var(--teal);color:var(--white);font-family:Arimo,sans-serif;font-size:12px}

  .events{left:0;top:493px;width:515px;height:201px;background:var(--teal)}
  .events .section-title{text-align:center;margin-top:16px}
  .event-card{top:52px;width:139px;height:118px;background:var(--sky);display:flex}
  .event-card__tab{width:25px;background:var(--turquoise);position:relative}
  .event-card__tab span{position:absolute;left:50%;top:8px;transform:translateX(-50%) rotate(180deg);writing-mode:vertical-rl;color:var(--white);font-weight:800;font-size:13px;letter-spacing:.5px}
  .event-card:nth-of-type(1){left:33px}
  .event-card:nth-of-type(2){left:188px}
  .event-card:nth-of-type(3){left:345px}

  .tech{left:0;top:698px;width:515px;height:146px;background:var(--grey)}
  .tech__photo{left:38px;top:13px;width:98px;height:98px;background:linear-gradient(135deg,#f4f4f4 0%,#c9c3cf 50%,#f1f1f1 100%)}
  .tech__title{left:171px;top:13px;font-size:21px;font-weight:800;color:var(--teal)}
  .tech__text{left:171px;top:44px;width:295px;font-family:Arimo,sans-serif;font-size:10.2px;line-height:1.3;text-align:justify;color:var(--ink)}

  /* back page */
  .sidebar{left:358px;top:0;width:157px;height:666px;background:var(--sky);text-align:center}
  .back-brand{left:0;width:157px;justify-content:center;top:64px;font-size:9px;gap:5px}
  .back-brand .brand__dot{width:8px;height:8px}
  .sidebar__title{position:absolute;left:0;width:157px;top:106px;font-size:14px;font-weight:800;color:#4b4b4b}
  .bar-title{left:0;width:355px;height:27px;background:var(--teal);color:var(--white);font-weight:800;font-size:14.5px;padding:4px 0 0 24px;letter-spacing:.3px}
  .note-title{top:4px}
  .news-title{top:356px}
  .doctor__name{left:24px;top:41px;font-family:"PT Sans Narrow",sans-serif;font-weight:700;font-size:14px;color:#222}
  .doctor__role{left:24px;top:58px;font-family:"PT Sans Narrow",sans-serif;font-weight:700;font-size:6.5px;color:#222}
  .doctor__photo{left:243px;top:70px;width:80px;height:80px;background:linear-gradient(160deg,#c9b5a4 0%,#7b5a48 55%,#b98a78 100%)}
  .body-copy{font-family:"PT Sans Narrow",sans-serif;font-size:9.3px;line-height:1.3;color:#333}
  .body-copy p{margin-bottom:9px}
  .note__lead{left:24px;top:73px;width:212px}
  .note__rest{left:24px;top:156px;width:320px}
  .news__photo{left:21px;top:391px;width:312px;height:149px;background:linear-gradient(90deg,#c7b8aa 0%,#d7c3b1 40%,#8a7b72 65%,#e4e0dc 100%)}
  .news__text{left:24px;top:551px;width:310px;font-style:italic}
  .listen{left:0;top:673px;width:515px;height:90px;background:#f6f6f6;border-top:2px solid var(--grey)}
  .listen__tab{left:0;top:11px;width:150px;height:64px;background:var(--turquoise);border-radius:0 10px 10px 0;color:var(--white);font-weight:800;font-size:14.5px;line-height:1.2;padding:12px 0 0 23px}
  .listen__text{left:164px;top:17px;width:334px}
  .footer{left:0;top:763px;width:515px;height:81px;background:var(--teal);color:var(--white)}
  .footer .social{color:var(--white)}
  .footer .social__icon{background:var(--white)}
  .back-social-1{left:25px;top:37px}
  .back-social-2{left:141px;top:37px}
  .footer__web{right:24px;top:40px;font-family:"PT Sans Narrow",sans-serif;font-size:9px}
</style>
</head>
<body>

<section class="page page--front">
  <div class="brand front-brand"><span class="brand__dot"></span>ORCHARD VALE AUDIOLOGY</div>
  <h1 class="abs masthead__title">HEARING CARE <span>FOR ALL AGES</span></h1>
  <div class="abs masthead__label">NEWSLETTER</div>
  <div class="abs social-row front-socials">
    <div class="social"><span class="social__icon"></span>orchardvalekids</div>
    <div class="social"><span class="social__icon"></span>orchardvaleaudiology</div>
  </div>

  <div class="abs edition-bar edition-bar--a"></div>
  <div class="abs edition-bar edition-bar--b"></div>
  <div class="abs edition-bar edition-bar--c">MONTHLY EDITION <span>February 2018</span></div>

  <div class="abs spotlight">
    <h2 class="section-title">PATIENT SPOTLIGHT</h2>
    <div class="abs spotlight__photo" role="img" aria-label="Photo of the clinic storefront"></div>
    <p class="abs spotlight__text">Lorem ipsum dolor sit amet, consectetuer adipiscing elit, sed diam nonummy nibh euismod tincidunt ut laoreet dolore magna aliquam erat volutpat. Ut wisi enim ad minim veniam, quis nostrud exerci tation ullamcorper suscipit lobortis nisl ut aliquip ex ea commodo consequat. Duis autem vel eum iriure dolor in hendrerit in vulputate velit esse molestie consequat, vel illum dolore eu feugiat nulla facilisis at vero eros et accumsan et iusto odio dignissim qui blandit praesent luptatum zzril delenit augue duis dolore te feugait nulla facilisi.</p>
  </div>

  <div class="abs evaluation">
    <h2>Ready for a hearing evaluation?</h2>
    <p>If you are ready for a start on the road to better hearing, call us today</p>
    <div class="evaluation__phone">(555) 014-2290</div>
  </div>

  <div class="abs events">
    <h2 class="section-title">UPCOMING EVENTS</h2>
    <div class="abs event-card"><div class="event-card__tab"><span>EVENT 1</span></div></div>
    <div class="abs event-card"><div class="event-card__tab"><span>EVENT 2</span></div></div>
    <div class="abs event-card"><div class="event-card__tab"><span>EVENT 3</span></div></div>
  </div>

  <div class="abs tech">
    <div class="abs tech__photo" role="img" aria-label="Photo of colourful custom ear moulds"></div>
    <h2 class="abs tech__title">TECHNOLOGY UPDATE</h2>
    <p class="abs tech__text">Lorem ipsum dolor sit amet, consectetuer adipiscing elit, sed diam nonummy nibh euismod tincidunt ut laoreet dolore magna aliquam erat volutpat. Ut wisi enim ad minim veniam, quis nostrud exerci tation ullamcorper suscipit lobortis nisl ut aliquip ex ea commodo consequat. Duis autem vel eum iriure dolor.</p>
  </div>
</section>

<section class="page page--back">
  <aside class="abs sidebar">
    <div class="brand back-brand"><span class="brand__dot"></span>ORCHARD VALE AUDIOLOGY</div>
    <h2 class="sidebar__title">Pediatric Corner</h2>
  </aside>

  <h2 class="abs bar-title note-title">A NOTE FROM DR. FENWICK</h2>
  <div class="abs doctor__name">Dana Fenwick, AuD, BC, PASC</div>
  <div class="abs doctor__role">Doctor of Audiology</div>
  <div class="abs doctor__photo" role="img" aria-label="Portrait photo of the audiologist"></div>
  <div class="abs body-copy note__lead"><p>Lorem ipsum dolor sit amet, consectetuer adipiscing elit, sed diam nonummy nibh euismod tincidunt ut laoreet dolore magna aliquam erat volutpat. Ut wisi enim ad minim veniam, quis nostrud exerci tation ullamcorper suscipit lobortis nisl ut aliquip ex ea commodo consequat. Duis autem vel eum iriure dolor in hendrerit in vulputate velit.</p></div>
  <div class="abs body-copy note__rest">
    <p>Vel illum dolore eu feugiat nulla facilisis at vero eros et accumsan et iusto odio dignissim qui blandit praesent luptatum zzril delenit augue duis dolore te feugait nulla facilisi. Nam liber tempor cum soluta nobis eleifend option congue nihil imperdiet doming id quod mazim placerat facer possim assum.</p>
    <p>Typi non habent claritatem insitam; est usus legentis in iis qui facit eorum claritatem. Investigationes demonstraverunt lectores legere me lius quod ii legunt saepius. Claritas est etiam processus dynamicus, qui sequitur mutationem consuetudium lectorum.</p>
    <p>Mirum est notare quam littera gothica, quam nunc putamus parum claram, anteposuerit litterarum formas humanitatis per seacula quarta decima et quinta decima. Eodem modo typi, qui nunc nobis videntur parum clari, fiant sollemnes in futurum. Lorem ipsum dolor sit amet, consectetuer adipiscing elit, sed diam nonummy nibh euismod tincidunt ut laoreet dolore magna aliquam erat volutpat. Ut wisi enim ad minim veniam,</p>
  </div>

  <h2 class="abs bar-title news-title">EXCITING NEWS</h2>
  <div class="abs news__photo" role="img" aria-label="Photo of an audiologist examining a patient's ear"></div>
  <div class="abs body-copy news__text">
    <p>Lorem ipsum dolor sit amet, consectetuer adipiscing elit, sed diam nonummy nibh euismod tincidunt ut laoreet dolore magna aliquam erat volutpat. Ut wisi enim ad minim veniam, quis nostrud exerci tation ullamcorper suscipit lobortis nisl ut aliquip ex ea commodo consequat.</p>
    <p>Duis autem vel eum iriure dolor in hendrerit in vulputate velit esse molestie consequat, vel illum dolore eu feugiat nulla facilisis at vero eros et accumsan et iusto odio dignissim qui blandit praesent luptatum zzril delenit augue duis dolore te feugait nulla facilisi.</p>
  </div>

  <div class="abs listen">
    <h2 class="abs listen__tab">LEARN TO<br>LISTEN</h2>
    <p class="abs body-copy listen__text">Vel illum dolore eu feugiat nulla facilisis at vero eros et accumsan et iusto odio dignissim qui blandit praesent luptatum zzril delenit augue duis dolore te feugait nulla facilisi. Nam liber tempor cum soluta nobis eleifend option congue nihil imperdiet doming id quod mazim placerat facer possim assum.</p>
  </div>

  <footer class="abs footer">
    <div class="abs social back-social-1"><span class="social__icon"></span>orchardvalekids</div>
    <div class="abs social back-social-2"><span class="social__icon"></span>orchardvaleaudiology</div>
    <div class="abs footer__web">www.orchardvalehearing.example</div>
  </footer>
</section>

</body>
</html>
```